Harbor Nightclub

Nightclub flyer., digital single sided, for KV and PX. I included samples of some previous flyers we've used. Sample Info:
HARBOR
FRIDAYS
FRI MAY 1 2020
DJ VORTAN (club floor)
DJ RUZO & DJ TAV (residents on the lounge floor)
4217 Marlow Avenue Sacramento
www.harborvenuehall.example for list/VIP inquiries

Target Market(s)

Upscale top 40 crowd but want some cool and artsy like the examples included.

Font styles to use
Sans Serif

Requirements
Must have
• Harbor Logo
Nice to have
• Would be nice if the flyer can be incorporated later with DJ photos (sometimes we will add dj photos to pixagram etc). Would like a big city type of feel.
Should not have
• Nothing too sexual.

```html
<!DOCTYPE html>
<html lang="en">
<head>
<meta charset="utf-8">
<title>Harbor Nightclub — Fridays</title>
<link rel="stylesheet" href="https://fonts.googleapis.com/css2?family=Roboto:wght@400;500&family=Roboto+Condensed:wght@300;400&family=Open+Sans:wght@400&display=swap">
<style>
  :root {
    --gold-deep: #7a4f1e;
    --gold-mid: #b8871f;
    --gold-bright: #ffcc0a;
    --brown: #6e3f22;
    --night: #0f0a14;
    --night-violet: #2a1d45;
    --white: #ffffff;
    --logo-olive: #b9ba64;
  }
  html, body {
    margin: 0;
    padding: 0;
    width: 848px;
    height: 1200px;
    overflow: hidden;
    background: var(--night);
  }
  .flyer {
    position: relative;
    width: 848px;
    height: 1200px;
    overflow: hidden;
    font-family: "Roboto", Arial, sans-serif;
    color: var(--white);
  }
  .flyer p, .flyer h1, .flyer ul { margin: 0; }
  .street-scene {
    position: absolute;
    inset: 0;
    background:
      radial-gradient(ellipse 420px 300px at 180px 720px, rgba(168,69,28,0.85), transparent 70%),
      radial-gradient(ellipse 300px 200px at 760px 380px, rgba(120,80,40,0.45), transparent 70%),
      radial-gradient(ellipse 500px 260px at 300px 300px, rgba(90,55,50,0.6), transparent 70%),
      linear-gradient(180deg, #1d1426 0%, var(--night-violet) 45%, #120c18 70%, var(--night) 100%);
  }
  .band {
    position: absolute;
    left: 0;
    width: 848px;
  }
  .band--top { top: 0; height: 210px; }
  .band--bottom { bottom: 0; height: 260px; }
  .address {
    position: absolute;
    top: 68px;
    left: 0;
    width: 848px;
    text-align: center;
    font-family: "Open Sans", Arial, sans-serif;
    font-size: 25px;
    line-height: 36px;
    letter-spacing: 0.3em;
    padding-left: 0.3em;
    box-sizing: border-box;
  }
  .headline {
    position: absolute;
    top: 224px;
    left: 0;
    width: 852px;
    text-align: center;
    font-family: "Roboto Condensed", "Arial Narrow", sans-serif;
    font-size: 145px;
    font-weight: 400;
    line-height: 1;
    letter-spacing: -0.01em;
  }
  .date {
    position: absolute;
    top: 370px;
    left: 0;
    width: 848px;
    text-align: center;
    font-size: 71px;
    font-weight: 500;
    line-height: 1;
    letter-spacing: 0.01em;
  }
  .lineup {
    position: absolute;
    top: 661px;
    left: 0;
    width: 848px;
    padding: 0;
    list-style: none;
    text-align: center;
    font-family: "Roboto Condensed", "Arial Narrow", sans-serif;
    font-size: 41px;
    line-height: 55px;
    letter-spacing: 0.04em;
  }
  .lineup li + li { margin-top: 42px; }
  .lineup .dj, .lineup .floor { display: block; }
  .ornament {
    position: absolute;
    left: 40px;
    top: 1000px;
    width: 580px;
    height: 80px;
  }
  .website {
    position: absolute;
    left: 62px;
    top: 1100px;
    font-family: "Open Sans", Arial, sans-serif;
    font-size: 19.5px;
    line-height: 24px;
  }
  .brand {
    position: absolute;
    left: 620px;
    top: 1013px;
    width: 166px;
    text-align: center;
  }
  .brand-mark {
    display: block;
    width: 64px;
    height: 64px;
    margin: 0 auto 10px;
    border-radius: 50%;
    background: var(--logo-olive);
  }
  .brand-name {
    font-family: "Roboto", Arial, sans-serif;
    font-weight: 500;
    font-size: 33px;
    line-height: 1;
    letter-spacing: 0.02em;
  }
</style>
</head>
<body>
<main class="flyer">
  <div class="street-scene" role="img" aria-label="Night street photo outside the club: a crowd queuing on the sidewalk and an orange sports car parked at the curb"></div>

  <svg class="band band--top" viewBox="0 0 848 210" preserveAspectRatio="none" aria-hidden="true">
    <defs>
      <linearGradient id="goldTop" x1="0" x2="1" y1="0" y2="0">
        <stop offset="0" stop-color="#7a4f1e"/>
        <stop offset="0.5" stop-color="#ffcc0a"/>
        <stop offset="1" stop-color="#7a4f1e"/>
      </linearGradient>
    </defs>
    <path d="M0 0 H848 V148 L420 203 L0 146 Z" fill="url(#goldTop)"/>
  </svg>

  <p class="address">4217 MARLOW AVENUE SACRAMENTO</p>

  <h1 class="headline">FRIDAYS</h1>
  <p class="date">MAY 1 2020</p>

  <ul class="lineup">
    <li><span class="dj">DJ VORTAN</span><span class="floor">(CLUB FLOOR)</span></li>
    <li><span class="dj">DJ RUZO &amp; DJ TAV</span><span class="floor">(RESIDENTS ON THE LOUNGE FLOOR)</span></li>
  </ul>

  <svg class="band band--bottom" viewBox="0 0 848 260" preserveAspectRatio="none" aria-hidden="true">
    <defs>
      <linearGradient id="goldBottom" x1="0" x2="1" y1="0" y2="0">
        <stop offset="0" stop-color="#6e3f22"/>
        <stop offset="0.5" stop-color="#b8871f"/>
        <stop offset="1" stop-color="#6e3f22"/>
      </linearGradient>
      <linearGradient id="goldFade" x1="0" x2="0" y1="0" y2="1">
        <stop offset="0" stop-color="#6e3f22" stop-opacity="0"/>
        <stop offset="1" stop-color="#ffcc0a" stop-opacity="0.35"/>
      </linearGradient>
    </defs>
    <path d="M0 16 C120 0 260 14 340 48 C380 62 410 52 425 27 C440 52 470 62 510 48 C590 14 730 -2 848 8 V260 H0 Z" fill="url(#goldBottom)"/>
    <path d="M0 16 C120 0 260 14 340 48 C380 62 410 52 425 27 C440 52 470 62 510 48 C590 14 730 -2 848 8 V260 H0 Z" fill="url(#goldFade)"/>
  </svg>

  <div class="ornament" role="img" aria-label="Decorative gold scrollwork flourish"></div>

  <p class="website">www.harborvenuehall.example for list/VIP inquiries</p>

  <div class="brand">
    <span class="brand-mark"></span>
    <div class="brand-name">HARBOR</div>
  </div>
</main>
</body>
</html>
```